Brochure Design Project for Home Watch company

We are a new start up company in fast growing home watch industry. We provide services in Hawaii so the design needs to be reflect that. Our web site can give you overview of what we do - www.palmcrestkeeper.com. We will service clients that own second homes in Hawaii. These properties are not necessarily income producing properties for our clients. I'm looking for 2 or 4 page brochure which will be used to market our services to potential new clients. It needs to be high quality, modern with slight Hawaiian feel (we are based on Oahu). I'm not looking for a trifold type of brochure.

We are open to various colors based on what the designer might suggest but as you can see on our home page - the main picture of the home on our site has lots of red and white which we like as well as the "head" or dot above the "i" in our logo is red. I was not able to upload the file of the main house (purchased on snapvaultpix) on here therefore I'll have to provide the original photo to the selected designer at the later time. For now I just uploaded the not purchased copy.

If you have other questions please do let me know. And lastly, I will be looking to create a business card and post card as well.

```html
<!DOCTYPE html>
<html lang="en">
<head>
<meta charset="utf-8">
<title>Palmcrest Keeper – Brochure</title>
<link rel="stylesheet" href="https://fonts.googleapis.com/css2?family=Oswald:wght@500;600&family=Roboto:wght@400;500;700&family=Roboto+Condensed:wght@700&display=swap">
<style>
:root{
  --red:#e8504f;
  --red-deep:#d63d3c;
  --ink:#1f1f1f;
  --body:#4a4a4a;
  --paper:#ffffff;
  --backdrop:#dcdcdc;
  --sea-top:#a9cfe6;
  --sea-mid:#5a9cc2;
  --sea-low:#2f5f7e;
}
*{margin:0;padding:0;box-sizing:border-box}
html,body{width:1200px;height:799px;overflow:hidden;background:var(--backdrop)}
body{position:relative;font-family:"Roboto",Arial,sans-serif;color:var(--body)}
.page{position:absolute;top:70px;width:435px;height:624px;background:var(--paper);overflow:hidden}
.page--front{left:130px}
.page--back{left:655px;width:437px}
.shape{position:absolute;left:0;top:0}
.brand{position:absolute;text-align:center}
.brand__name{font-family:"Roboto",sans-serif;font-weight:700;color:var(--ink);display:flex;align-items:center;gap:5px;justify-content:center}
.brand__dot{width:9px;height:9px;border-radius:50%;background:var(--red);display:inline-block}
.brand__tag{font-size:7.5px;color:var(--ink);margin-top:3px}
.headline{position:absolute;left:12px;top:282px;font-family:"Oswald",sans-serif;line-height:1.05}
.headline__main{font-size:17px;font-weight:600;color:var(--ink);letter-spacing:.2px}
.headline__sub{font-size:13px;font-weight:500;color:var(--red)}
.devices{position:absolute;left:250px;top:282px;width:112px;height:62px;background:linear-gradient(135deg,#3a3a3a,#8fb6cf 55%,#eeeeee);border-radius:3px}
.tab{position:absolute;height:13px;background:var(--red);color:#fff;font-family:"Oswald",sans-serif;font-weight:500;font-size:8px;line-height:13px;padding:0 9px;letter-spacing:.3px}
.tab--left{left:0;border-radius:0 7px 7px 0}
.tab--right{right:0;border-radius:7px 0 0 7px}
.rule{position:absolute;height:1px;background:var(--red)}
.copy{position:absolute;font-size:5.6px;line-height:1.45;color:var(--body)}
.copy p{margin-bottom:4px}
.copy h3{font-family:"Roboto Condensed",sans-serif;font-weight:700;color:var(--red);font-size:8.4px;margin:2px 0 3px}
.values{list-style:none}
.values li{font-weight:700;color:var(--ink);margin-bottom:4px;padding-left:6px;position:relative}
.values li::before{content:"";position:absolute;left:0;top:2px;width:3px;height:3px;background:var(--red);border-radius:50%}
.contact{position:absolute;color:#fff;font-size:7.5px;letter-spacing:.4px;display:flex;align-items:center;gap:4px}
.contact svg{flex:none}
.badge{position:absolute;width:38px;height:14px;background:#d9e1ee;border-radius:1px}
</style>
</head>
<body>

<section class="page page--front">
  <svg class="shape" width="435" height="624" viewBox="0 0 435 624">
    <defs>
      <linearGradient id="frontSea" x1="0" y1="0" x2="0" y2="1">
        <stop offset="0" stop-color="var(--sea-top)"/>
        <stop offset=".45" stop-color="#d9d3cc"/>
        <stop offset=".7" stop-color="var(--sea-mid)"/>
        <stop offset="1" stop-color="var(--sea-low)"/>
      </linearGradient>
    </defs>
    <rect role="img" aria-label="Photo of a Hawaiian villa with an infinity pool overlooking the ocean" x="0" y="0" width="435" height="236" fill="url(#frontSea)"/>
    <path d="M0,205 Q110,180 165,208 Q217,168 270,208 Q325,180 435,205 L435,236 L0,236Z" fill="var(--red)"/>
    <path d="M0,222 Q110,200 165,222 Q217,180 270,222 Q325,200 435,222 L435,245 L0,245Z" fill="var(--paper)"/>
    <path d="M0,596 Q80,586 160,594 Q217,578 275,594 Q355,586 435,596 L435,624 L0,624Z" fill="var(--red)"/>
  </svg>

  <div class="brand" style="left:140px;top:226px;width:155px">
    <div class="brand__name" style="font-size:11.5px"><span class="brand__dot"></span>Palmcrest Keeper</div>
    <div class="brand__tag">Your Home Watch Company</div>
  </div>

  <div class="headline">
    <div class="headline__main">PROVIDING PREMIERE HOME</div>
    <div class="headline__sub">WATCH AND CONCIERGE SERVICES</div>
  </div>
  <div class="devices" role="img" aria-label="Illustration of a laptop and tablet showing a home and checklist"></div>

  <div class="rule" style="left:0;top:342px;width:435px"></div>
  <div class="tab tab--left" style="top:336px">WHAT DO WE DO?</div>
  <div class="copy" style="left:12px;top:355px;width:225px">
    <p>We save your time. We perform visual inspections and provide our presence while you are away so you can enjoy your time and home while you are on the island. We have your back!</p>
  </div>

  <div class="rule" style="left:0;top:401px;width:435px"></div>
  <div class="tab tab--left" style="top:395px">WHO WE ARE?</div>
  <div class="tab tab--right" style="top:395px">SERVICES</div>

  <div class="copy" style="left:12px;top:413px;width:198px">
    <h3>We are a family run and operated business</h3>
    <p>Leilani is licensed real estate broker in Hawaii. She has 10+ years' work experience at a major global commercial real estate company.</p>
    <p>Kekoa owns a handyman and landscaping firm that is based on two simple principles: Pay extra attention to details, and under promise and over deliver!</p>
    <p>We both put our hearts and souls into what we do. Internally, we are led by 5 principles that define us, as well as everything we do in a daily life:</p>
    <ul class="values">
      <li>High moral and ethical values;</li>
      <li>Passionate and hard-working attitude;</li>
      <li>Enhanced attention to details;</li>
      <li>Awareness of social responsibility in our professional and personal life;</li>
      <li>Choosing sustainable practices whenever possible.</li>
    </ul>
  </div>

  <div class="copy" style="left:222px;top:413px;width:202px">
    <h3>General Outdoor Visual Inspections</h3>
    <p>Check yard, lawn and landscaping; check lanai, deck, and pool area for any damage; check for mold or fading of all outdoor furniture; check water level of swimming pool or hot tub, if applicable</p>
    <h3>Home Exterior Visual Inspections</h3>
    <p>Check security cameras; check for overall damage; remove mail, newspapers, and flyers from mailbox and store inside of the property; check outdoor plumbing and hoses for leakage; check garage; check for vandalism and theft</p>
    <h3>Home Interior Visual Inspections</h3>
    <p>Make sure security system is in working order; ensure that all doors, windows and sliders are locked and secured; check thermostats and make sure the air conditioning is set at appropriate and requested temperature; make sure all smoke detectors are in proper working order or replace batteries if necessary</p>
  </div>

  <div class="contact" style="left:14px;top:596px">
    <svg width="7" height="7" viewBox="0 0 10 10"><circle cx="5" cy="5" r="4.3" fill="none" stroke="#fff" stroke-width="1.2"/><path d="M1,5H9M5,1Q2,5 5,9Q8,5 5,1" fill="none" stroke="#fff" stroke-width=".9"/></svg>
    www.palmcrestkeeper.com
  </div>
  <div class="contact" style="left:14px;top:609px">
    <svg width="6" height="8" viewBox="0 0 6 10"><rect x=".6" y=".6" width="4.8" height="8.8" rx="1" fill="none" stroke="#fff" stroke-width="1.1"/></svg>
    808-555-0142
  </div>
</section>

<section class="page page--back">
  <svg class="shape" width="437" height="624" viewBox="0 0 437 624">
    <defs>
      <linearGradient id="backSea" x1="0" y1="0" x2="1" y2="1">
        <stop offset="0" stop-color="var(--sea-top)"/>
        <stop offset=".4" stop-color="#7a8e84"/>
        <stop offset=".7" stop-color="#3a9fd0"/>
        <stop offset="1" stop-color="var(--sea-low)"/>
      </linearGradient>
      <linearGradient id="haze" x1="0" y1="0" x2="1" y2="0">
        <stop offset="0" stop-color="#f1f1f1"/>
        <stop offset="1" stop-color="#ffffff"/>
      </linearGradient>
    </defs>
    <rect x="0" y="0" width="437" height="275" fill="url(#haze)"/>
    <path role="img" aria-label="Photo of a modern villa with a long lap pool above the coast" d="M0,0 H215 Q150,90 165,175 Q175,225 225,262 L0,262Z" fill="url(#backSea)"/>
    <path d="M215,0 H232 Q165,90 178,172 Q190,225 245,268 L225,262 Q175,225 165,175 Q150,90 215,0Z" fill="var(--red)"/>
    <path d="M232,0 H238 Q175,92 188,172 Q200,228 260,270 L245,268 Q190,225 178,172 Q165,90 232,0Z" fill="var(--ink)"/>
    <path d="M0,250 Q200,300 437,240 L437,262 Q220,300 0,270Z" fill="var(--red)"/>
    <path d="M0,258 Q210,296 437,252 L437,256 Q210,300 0,262Z" fill="var(--ink)"/>
    <path d="M0,266 Q220,302 437,256 L437,284 L0,284Z" fill="var(--paper)"/>
    <path d="M0,596 Q80,586 160,594 Q217,578 275,594 Q355,586 437,596 L437,624 L0,624Z" fill="var(--red)"/>
  </svg>

  <div class="brand" style="left:215px;top:118px;width:190px">
    <div class="brand__name" style="font-size:15px"><span class="brand__dot" style="width:11px;height:11px"></span>Palmcrest Keeper</div>
    <div class="brand__tag" style="font-size:9.5px">Your Home Watch Company</div>
  </div>

  <div class="rule" style="left:0;top:285px;width:437px"></div>
  <div class="tab tab--left" style="top:279px">WHAT IS A HOME WATCH?</div>
  <div class="tab tab--right" style="top:279px">CONCIERGE SERVICES</div>

  <div class="copy" style="left:12px;top:297px;width:200px">
    <p>Home watch is a visual inspection of a vacant home or a vacation rental property where we look for obvious issues and report our findings to you, the client. We can also coordinate maintenance and repair services as well as provide a wide range of concierge services.</p>
  </div>

  <div class="rule" style="left:0;top:350px;width:215px"></div>
  <div class="tab tab--left" style="top:344px">OUR MISSION</div>
  <div class="copy" style="left:12px;top:362px;width:200px">
    <p>Palmcrest Keeper's mission is to deliver superior, reliable and individually tailored services to our clients in the utmost ethical and professional manner possible.</p>
    <p>Therefore, we are here to serve you, fill in the void during your absence, ease your worries, be your eyes and ears (and many times, hands and feet as well) on the ground, and ensure your peace of mind and good night' sleep. We pledge to treat your property like it was our own while you are away and unable to do so yourself. Whether your property is your second home gateway, or you travel for extended periods of time, Palmcrest Keeper provides visual property inspections, minor landscaping, handyman and housekeeping services, various vendor coordination, and offer various concierge services customized to your specific needs.</p>
  </div>
  <div role="img" aria-label="Cutaway illustration of a house with service icons around it" style="position:absolute;left:58px;top:462px;width:110px;height:118px;background:linear-gradient(180deg,#f6dcdc,#e9e9e9);border-radius:4px"></div>

  <div class="copy" style="left:225px;top:296px;width:202px">
    <h3>Pre-Arrival</h3>
    <p>Groceries purchased and stored, air conditioning and ceiling vents turned on and/or windows opened, water turned on, flowers placed, fresh laundered linens on beds, towels arranged in the bathrooms, deck furniture placed on decks and patio, house freshened up and aired out, security system disarmed as appropriate, decks, walkways, lanais, and driveways cleaned of debris and special requestes completed.</p>
    <h3>Post-Departure</h3>
    <p>House cleaning coordinated, beds made, sheets and towels cleaned, dishes washed and put away, all doors and windows secured, lights on timers set, water turned off, outdoor furniture stored or covered per specific instructions, driveways, lanais, walkways and decks cleared of debris, air conditioning set to appropriate level, trash placed for collection and security system turned on.</p>
    <h3>Sample of Special Services</h3>
    <p>Key holding services, mail forwarding, coordination of transportation from and to the airport, light handyman and landscaping services, vendor coordination (we coordinate access and meet everyone you authorize at your home including but not limited to maintenance, repair, pest control, landscaping and tree trimming, and utility providers), pre-storm services (secure outdoor furniture, potted plants, hammocks and any other outdoor items, etc.) and post-storm services (clean walkway and driveway, pick-up trash, etc.), and emergency services response, etc. Additional services and pricing available upon request.</p>
    <h3>Member of NRWG</h3>
    <p style="width:140px">We are Accredited Members of the NRWG. We are insured and bonded, and we agreed to uphold the strictest and most ethical standards in the industry</p>
  </div>
  <div class="badge" style="left:378px;top:545px"></div>

  <div class="contact" style="left:14px;top:596px">
    <svg width="6" height="8" viewBox="0 0 6 9"><path d="M3,8.5Q.4,5 .4,3A2.6,2.6 0 0 1 5.6,3Q5.6,5 3,8.5Z" fill="#fff"/><circle cx="3" cy="3" r="1" fill="var(--red)"/></svg>
    Palmcrest Keeper LLC
  </div>
  <div class="contact" style="left:24px;top:609px">Honolulu Hawaii</div>
  <div class="contact" style="left:225px;top:596px">
    <svg width="7" height="7" viewBox="0 0 10 10"><circle cx="5" cy="5" r="4.3" fill="none" stroke="#fff" stroke-width="1.2"/><path d="M1,5H9M5,1Q2,5 5,9Q8,5 5,1" fill="none" stroke="#fff" stroke-width=".9"/></svg>
    www.palmcrestkeeper.com
  </div>
  <div class="contact" style="left:225px;top:609px">
    <svg width="6" height="8" viewBox="0 0 6 10"><rect x=".6" y=".6" width="4.8" height="8.8" rx="1" fill="none" stroke="#fff" stroke-width="1.1"/></svg>
    808-555-0142
  </div>
</section>

</body>
</html>
```